Business Card Design

It's an investment advisory service for individuals with all there investment needs. Also financial consulting to businesses and governmental agencies on retirement plans etc. It's personalized not commoditized help. Should show strength, knowledge and money orientation.

Industry/Entity Type

Investment

Contact Information for Business Card

B. Vel R. Financial Consulting and Wealth Management, Mirek Dale Hopstein, 5172 Paseo Las Colinas Verde, San Diego, CA 92084-6617, Registered Investment Advisor

Requirements
Nice to have
• Something money oriented

```html
<!DOCTYPE html>
<html lang="en">
<head>
<meta charset="utf-8">
<title>B. Vel R. Financial Consulting – Business Cards</title>
<link href="https://fonts.googleapis.com/css2?family=Sorts+Mill+Goudy&family=Cormorant+Garamond:wght@500;700&display=swap" rel="stylesheet">
<style>
  :root {
    --stage: #000000;
    --brand-green: #3b7b3f;
    --deep-green: #2f6a36;
    --soft-green: #cfe0c9;
    --pale-green: #e6efe2;
    --ink: #1e1e1e;
    --white: #ffffff;
  }
  html, body {
    margin: 0;
    padding: 0;
    width: 1200px;
    height: 1000px;
    overflow: hidden;
    background: var(--stage);
  }
  .canvas {
    position: relative;
    width: 1200px;
    height: 1000px;
    background: var(--stage);
  }
  .card {
    position: absolute;
    left: 248px;
    width: 760px;
    overflow: hidden;
    background: var(--white);
    font-family: "Sorts Mill Goudy", "Cormorant Garamond", serif;
  }
  .card--money { top: 52px; height: 433px;
    background: linear-gradient(180deg, #f4f6f2 0%, #ffffff 62%, #e9f0e6 75%, #7fa67c 90%, var(--deep-green) 100%);
  }
  .card--markets { top: 513px; height: 432px;
    background:
      radial-gradient(ellipse 62% 60% at 55% 42%, #ffffff 0%, #f6f9f4 45%, rgba(255,255,255,0) 80%),
      linear-gradient(180deg, #8fb28b 0%, #e4ede1 25%, #f4f7f2 55%, #bcd2b7 80%, var(--deep-green) 100%);
  }
  .edge {
    position: absolute;
    top: 0;
    bottom: 0;
    background: linear-gradient(180deg, var(--soft-green), #b9d0b3 70%, #6f9a6c);
  }
  .edge--left { left: 0; width: 10px; }
  .edge--right { right: 0; width: 28px; }
  .banknote-art {
    position: absolute;
    left: 10px;
    top: 0;
    width: 722px;
    height: 300px;
    background: linear-gradient(165deg, #dfe6da 0%, #ecf0e8 45%, #f7f8f5 75%, rgba(255,255,255,0) 100%);
  }
  .market-art {
    position: absolute;
    left: 345px;
    top: 222px;
    width: 335px;
    height: 168px;
    border-radius: 40% 40% 20% 20%;
    background: radial-gradient(ellipse at 50% 60%, #6d9a69 0%, #8fb08b 55%, rgba(143,176,139,0) 80%);
  }
  .brand-block {
    position: absolute;
    left: 0;
    background: var(--brand-green);
    color: var(--white);
    text-align: center;
  }
  .card--money .brand-block { top: 92px; width: 247px; height: 229px; }
  .card--markets .brand-block { top: 43px; width: 253px; height: 240px; }
  .brand-name {
    margin: 44px 0 0;
    font-size: 48px;
    line-height: 1;
    font-weight: 400;
    letter-spacing: 1px;
  }
  .card--markets .brand-name { margin-top: 50px; }
  .brand-rule {
    width: 190px;
    height: 2px;
    margin: 18px auto 8px;
    background: var(--white);
    border-radius: 50%;
  }
  .brand-tagline {
    font-size: 15px;
    line-height: 19px;
    letter-spacing: 0.3px;
    text-transform: uppercase;
  }
  .brand-rule--lower { margin: 8px auto 0; }
  .contact {
    position: absolute;
    right: 66px;
    text-align: right;
    color: var(--ink);
  }
  .card--money .contact { top: 156px; }
  .card--markets .contact { top: 57px; right: 64px; }
  .person-name {
    margin: 0;
    font-family: "Cormorant Garamond", serif;
    font-weight: 700;
    font-size: 34px;
    line-height: 38px;
  }
  .credentials {
    color: var(--brand-green);
    font-size: 20px;
    line-height: 26px;
    margin-bottom: 34px;
  }
  .card--markets .credentials { margin-bottom: 12px; }
  .phone, .email { font-size: 23px; line-height: 31px; }
  .designation {
    position: absolute;
    left: 66px;
    right: 60px;
    bottom: 26px;
    color: var(--white);
    font-size: 20px;
    letter-spacing: 7.4px;
    text-align: right;
    text-transform: uppercase;
  }
</style>
</head>
<body>
<main class="canvas">

  <section class="card card--money">
    <div class="banknote-art" role="img" aria-label="Fanned hundred-dollar banknotes in pale green tones"></div>
    <div class="edge edge--left" role="img" aria-label="Banknote guilloche border"></div>
    <div class="edge edge--right" role="img" aria-label="Banknote guilloche border"></div>
    <div class="brand-block">
      <p class="brand-name">B. Vel R.</p>
      <div class="brand-rule"></div>
      <div class="brand-tagline">Financial Consulting<br>&amp; Wealth Management</div>
      <div class="brand-rule brand-rule--lower"></div>
    </div>
    <div class="contact">
      <h2 class="person-name">Mirek “Dale” Hopstein</h2>
      <div class="credentials">MBA, RP©, CRC©</div>
      <div class="phone">858-555-0142 / 775-555-0187</div>
      <div class="email">dale.hopstein@velrmail.com</div>
    </div>
    <div class="designation">Registered Investment Advisor</div>
  </section>

  <section class="card card--markets">
    <div class="edge edge--left" role="img" aria-label="Banknote guilloche border"></div>
    <div class="edge edge--right" role="img" aria-label="Banknote guilloche border"></div>
    <div class="market-art" role="img" aria-label="Engraved green bull and bear facing each other"></div>
    <div class="brand-block">
      <p class="brand-name">B. Vel R.</p>
      <div class="brand-rule"></div>
      <div class="brand-tagline">Financial Consulting<br>&amp; Wealth Management</div>
      <div class="brand-rule brand-rule--lower"></div>
    </div>
    <div class="contact">
      <h2 class="person-name">Mirek “Dale” Hopstein</h2>
      <div class="credentials">MBA, RP©, CRC©</div>
      <div class="phone">858-555-0142 / 775-555-0187</div>
      <div class="email">dale.hopstein@velrmail.com</div>
    </div>
    <div class="designation">Registered Investment Advisor</div>
  </section>

</main>
</body>
</html>
```